Casa Vero Inspections Business Card

I need a business card for my new company. The company is going to provide home inspections. The name of the company is Casa Vero Inspections. I am not sure if I want a single sided card or a double. I have a logo already that I want to incorporate into the card design. I was wondering if I should incorporate a catch phrase on my card or not. If I did the phrase would be "The Intelligent Choice for Home Inspections" but i am unsure how or if to use it on a card. The following information needs to be on the card.
Home Inspection
My Name: Marcus T. Wolford Phone Number: 555-301-7762 Email: mwolford@casaveroinspections.com Website: www.casaveroinspections.com NY HI License # 27300519462

```html
<!DOCTYPE html>
<html lang="en">
<head>
<meta charset="utf-8">
<title>Casa Vero Inspections – Business Card</title>
<link rel="stylesheet" href="https://fonts.googleapis.com/css2?family=Arimo&family=Montserrat:wght@700&family=Quicksand:wght@500&display=swap">
<style>
  :root {
    --backdrop: #c8c9c4;
    --ink: #000000;
    --paper: #ffffff;
    --blue-deep: #036aa9;
    --blue-sky: #77c5f0;
  }
  html, body {
    margin: 0;
    padding: 0;
    width: 1003px;
    height: 1200px;
    overflow: hidden;
    background: var(--backdrop);
  }
  .card {
    position: absolute;
    left: 140px;
    width: 722px;
    height: 390px;
    display: block;
  }
  .card--front { top: 155px; }
  .card--back { top: 630px; }
  .paper { fill: var(--paper); }
  .ink { fill: var(--ink); }
  .deep { fill: var(--blue-deep); }
  .sky { fill: var(--blue-sky); }
  .brand-name {
    font-family: "Montserrat", sans-serif;
    font-weight: 700;
    letter-spacing: 3px;
  }
  .brand-name--light { fill: var(--paper); }
  .brand-name--blue { fill: var(--blue-deep); }
  .contact {
    font-family: "Quicksand", sans-serif;
    font-weight: 500;
  }
  .contact--light { fill: var(--paper); }
  .contact--dark { fill: var(--ink); }
  .holder-name {
    font-family: "Arimo", Arial, sans-serif;
    fill: var(--paper);
  }
  .icon-line { fill: none; stroke: var(--paper); stroke-width: 3; stroke-linecap: round; stroke-linejoin: round; }
  .icon-fill { fill: var(--paper); }
</style>
</head>
<body>

<!-- Front of card -->
<svg class="card card--front" viewBox="0 0 1085 585" role="group" aria-label="Card front">
  <rect class="paper" width="1085" height="585"/>
  <polygon class="ink" points="0,0 1085,0 1085,245 543,440 0,178"/>
  <polygon class="deep" points="0,178 543,440 543,516"/>
  <polygon class="sky" points="543,440 1085,245 543,516"/>

  <rect class="sky" x="528" y="86" width="30" height="30"/>
  <text class="brand-name brand-name--light" x="543" y="210" font-size="58" text-anchor="middle">CASA VERO</text>
  <text class="brand-name brand-name--light" x="543" y="278" font-size="42" text-anchor="middle">INSPECTIONS</text>

  <text class="contact contact--dark" x="543" y="572" font-size="31" text-anchor="middle">www.casaveroinspections.com</text>
</svg>

<!-- Back of card -->
<svg class="card card--back" viewBox="0 0 1085 585" role="group" aria-label="Card back">
  <rect class="paper" width="1085" height="585"/>
  <polygon class="ink" points="0,0 1085,0 1085,104 497,520 0,372"/>
  <polygon class="deep" points="0,372 497,520 0,412"/>
  <polygon class="sky" points="0,412 497,520 497,585"/>
  <polygon class="sky" points="1085,104 1085,130 497,520"/>
  <polygon class="deep" points="1085,130 1085,145 497,585 497,520"/>

  <text class="holder-name" x="62" y="99" font-size="62">MARCUS T. WOLFORD</text>
  <rect class="paper" x="66" y="109" width="846" height="3"/>

  <!-- phone -->
  <rect class="deep" x="222" y="135" width="52" height="52"/>
  <path class="icon-fill" d="M238 148 l6 -3 l5 9 l-4 3 q3 7 9 11 l4 -3 l8 6 l-3 6 q-14 -2 -25 -29 z"/>
  <text class="contact contact--light" x="301" y="171" font-size="28">555-301-7762</text>

  <!-- email -->
  <rect class="deep" x="222" y="205" width="52" height="52"/>
  <rect class="icon-fill" x="235" y="223" width="26" height="17" rx="1"/>
  <path d="M236 224 l12 9 l12 -9" fill="none" stroke="#036aa9" stroke-width="2.5"/>
  <text class="contact contact--light" x="301" y="241" font-size="28">mwolford@casaveroinspections.com</text>

  <!-- license / pin -->
  <rect class="deep" x="222" y="283" width="52" height="52"/>
  <path class="icon-fill" d="M248 324 l-9 -15 a10 10 0 1 1 18 0 z"/>
  <circle cx="248" cy="303" r="4" fill="#036aa9"/>
  <text class="contact contact--light" x="301" y="319" font-size="25">NY HI License # 27300519462</text>

  <!-- web -->
  <rect class="deep" x="222" y="357" width="52" height="52"/>
  <circle class="icon-line" cx="248" cy="383" r="14"/>
  <ellipse class="icon-line" cx="248" cy="383" rx="6" ry="14"/>
  <line class="icon-line" x1="234" y1="383" x2="262" y2="383"/>
  <line class="icon-line" x1="236" y1="376" x2="260" y2="376"/>
  <line class="icon-line" x1="236" y1="390" x2="260" y2="390"/>
  <text class="contact contact--light" x="301" y="389" font-size="20">www.casaveroinspections.com</text>

  <rect class="deep" x="896" y="452" width="22" height="22"/>
  <text class="brand-name brand-name--blue" x="907" y="520" font-size="38" text-anchor="middle">CASA VERO</text>
  <text class="brand-name brand-name--blue" x="907" y="556" font-size="27" text-anchor="middle">INSPECTIONS</text>
</svg>

</body>
</html>
```